Create a bold and border around my logo to make it pop and sign graphic design

I would like someone to create a sign graphic design so I can use on the side of my trucks and put on yard signs. I would to remove a lot of the white and add more of the orange and blue to give it more pop when cars drive past. I would like the services to be removed and for you to leave space for a mobile number that i would add later. I don’t want my logo changed at all. I just want colour and design to be added to the background so i can use it in signage. Same colour as on the sign

```html
<!DOCTYPE html>
<html lang="en">
<head>
<meta charset="utf-8">
<title>Timberline Yard Sign</title>
<link rel="stylesheet" href="https://fonts.googleapis.com/css2?family=Montserrat:wght@700;800&family=Oswald:wght@600&display=swap">
<style>
  :root {
    --backdrop: #3d3d3d;
    --sign-blue: #3b459e;
    --sign-blue-deep: #333c8f;
    --sign-blue-light: #4a53aa;
    --orange: #f27a2b;
    --cream: #fbeee2;
    --white: #ffffff;
    --corner-fade: #8c4a78;
  }
  * { margin: 0; padding: 0; box-sizing: border-box; }
  html, body {
    width: 1200px;
    height: 572px;
    overflow: hidden;
    background: var(--backdrop);
  }
  .canvas {
    position: relative;
    width: 1200px;
    height: 572px;
    display: flex;
    align-items: center;
    justify-content: center;
  }
  .sign {
    position: relative;
    width: 840px;
    height: 560px;
    overflow: hidden;
    background: radial-gradient(ellipse at 60% 35%, var(--sign-blue-light), var(--sign-blue) 55%, var(--sign-blue-deep));
  }
  .sign-shapes {
    position: absolute;
    inset: 0;
    width: 840px;
    height: 560px;
  }
  .brand {
    position: absolute;
    left: 370px;
    top: 34px;
    width: 340px;
    display: flex;
    flex-direction: column;
    align-items: center;
  }
  .brand-dot {
    width: 190px;
    height: 190px;
    border-radius: 50%;
    background: var(--orange);
  }
  .brand-name {
    margin-top: 62px;
    font-family: "Montserrat", sans-serif;
    font-weight: 800;
    font-size: 48px;
    line-height: 1;
    letter-spacing: 1px;
    color: var(--orange);
    white-space: nowrap;
  }
  .contact {
    position: absolute;
    left: 213px;
    top: 440px;
    display: flex;
    align-items: center;
    gap: 35px;
  }
  .phone-badge {
    width: 75px;
    height: 75px;
    border-radius: 12px;
    background: var(--orange);
    display: flex;
    align-items: center;
    justify-content: center;
  }
  .phone-number {
    position: relative;
    top: -10px;
    font-family: "Oswald", sans-serif;
    font-weight: 600;
    font-size: 90px;
    line-height: 1;
    letter-spacing: 1px;
    color: var(--white);
    white-space: nowrap;
  }
</style>
</head>
<body>
<main class="canvas">
  <section class="sign">
    <svg class="sign-shapes" viewBox="0 0 840 560">
      <defs>
        <linearGradient id="tree-tone" x1="0" y1="0" x2="1" y2="0">
          <stop offset="0" stop-color="#f27a2b"/>
          <stop offset="0.45" stop-color="#f59a5e"/>
          <stop offset="1" stop-color="#fbeee2"/>
        </linearGradient>
        <linearGradient id="corner-tone" x1="0" y1="0" x2="0" y2="1">
          <stop offset="0" stop-color="#f27a2b"/>
          <stop offset="1" stop-color="#8c4a78"/>
        </linearGradient>
      </defs>
      <path class="tree-artwork" role="img" aria-label="Stylised cream tree with curling swirl branches on an orange panel"
            d="M0 0 H350 C360 120 300 190 270 230 C235 280 215 340 195 400 C180 450 205 520 230 560 H0 Z"
            fill="url(#tree-tone)"/>
      <path class="corner-accent" d="M730 0 H840 V263 Z" fill="url(#corner-tone)"/>
      <path class="corner-stripe" d="M748 100 L840 250 V262 L742 106 Z" fill="url(#corner-tone)" opacity="0.7"/>
      <path class="number-frame"
            d="M606 425 H797 Q809 425 809 437 V515 Q809 527 797 527 H390"
            fill="none" stroke="var(--orange)" stroke-width="2.5"/>
    </svg>

    <div class="brand">
      <div class="brand-dot"></div>
      <div class="brand-name">TIMBERLINE</div>
    </div>

    <div class="contact">
      <div class="phone-badge">
        <svg width="44" height="44" viewBox="0 0 24 24" aria-hidden="true">
          <path fill="#333c8f" d="M6.6 10.8a15.1 15.1 0 0 0 6.6 6.6l2.2-2.2a1 1 0 0 1 1-.25 11.4 11.4 0 0 0 3.6.57 1 1 0 0 1 1 1V20a1 1 0 0 1-1 1A17 17 0 0 1 3 4a1 1 0 0 1 1-1h3.5a1 1 0 0 1 1 1c0 1.25.2 2.45.57 3.57a1 1 0 0 1-.25 1z"/>
        </svg>
      </div>
      <div class="phone-number">0800 123 45</div>
    </div>
  </section>
</main>
</body>
</html>
```